Flyer Design for an electrical and security company trying to build local customers

I need a flyer design for a new company based in Sans Souci, Sydney 2219 called "Harbor Quill Dune Electrical and Security" also "HQD Electrical and Security". We are electrical contractors who are looking for more local work including emergency service calls and any project work including renovations or new constructions in the local area. I would like everyone in the area to know I am new and that I am available 24 hours a day 7 days a week. I would like to see designs that use the logo colours. Would also like the font of the entire design to be "juice bold".

Electrical

• juice bold

Requirements
Must have
• Must use the colours of the original logo and also have the information from the rear of the card. Must also have services buttons like the website picture attached.

```html
<!DOCTYPE html>
<html lang="en">
<head>
<meta charset="utf-8">
<title>Harbor Quill Dune Electrical and Security – Flyer</title>
<link rel="stylesheet" href="https://fonts.googleapis.com/css2?family=Exo+2:wght@500;600;700&display=swap">
<style>
  :root {
    --backdrop: #2b2b2d;
    --black: #0c0c0c;
    --white: #ffffff;
    --orange: #ef8a22;
    --blue: #4fb3e3;
    --ink: #1d1d1f;
    --photo-light: #b9c3cc;
    --photo-dark: #4d6479;
  }
  * { box-sizing: border-box; margin: 0; padding: 0; }
  html, body { width: 1200px; height: 659px; overflow: hidden; }
  body {
    background: var(--backdrop);
    font-family: "Exo 2", sans-serif;
    font-weight: 700;
    color: var(--white);
    display: flex;
    justify-content: center;
    align-items: center;
    gap: 70px;
  }
  .flyer {
    width: 410px;
    height: 580px;
    background: var(--black);
    position: relative;
    overflow: hidden;
    box-shadow: 0 10px 30px rgba(0,0,0,.45);
  }

  /* Front */
  .front-header {
    height: 170px;
    background: var(--white);
    display: flex;
    flex-direction: column;
    justify-content: center;
    align-items: center;
    color: var(--ink);
  }
  .brand-name {
    font-size: 30px;
    line-height: 1.05;
    text-align: center;
    color: var(--ink);
    font-weight: 700;
  }
  .brand-tagline {
    font-size: 12px;
    font-weight: 600;
    margin-top: 8px;
    letter-spacing: .5px;
  }
  .front-body {
    display: flex;
    padding: 34px 26px 0 30px;
    gap: 22px;
  }
  .services-copy {
    width: 178px;
    font-size: 13.5px;
    font-weight: 600;
    line-height: 1.28;
    text-align: justify;
    letter-spacing: 1px;
  }
  .call-panel {
    flex: 1;
    text-align: center;
  }
  .call-lead { font-size: 17px; }
  .call-hours {
    font-size: 54px;
    color: var(--orange);
    line-height: 1;
    margin: 2px 0;
  }
  .call-services { font-size: 20px; line-height: 1.05; font-weight: 600; }
  .call-divider {
    height: 2px;
    background: var(--white);
    margin: 22px 0 24px;
  }
  .call-promise { font-size: 17px; line-height: 1.2; }
  .front-contact {
    position: absolute;
    left: 30px; right: 26px;
    bottom: 26px;
    font-size: 14px;
    font-weight: 600;
    letter-spacing: .6px;
  }
  .contact-row {
    display: flex;
    justify-content: space-between;
    align-items: center;
    margin-bottom: 8px;
  }
  .contact-item { display: flex; align-items: center; gap: 7px; }
  .dot-mark {
    width: 18px; height: 18px;
    border-radius: 50%;
    background: var(--white);
    display: inline-block;
  }
  .contact-web { padding-left: 25px; }

  /* Back */
  .back-photo {
    height: 230px;
    background: linear-gradient(135deg, var(--photo-light) 0%, #8ea2b4 45%, var(--photo-dark) 100%);
  }
  .back-body {
    display: flex;
    padding: 26px 22px 0 22px;
    gap: 16px;
    height: 180px;
  }
  .back-brand {
    width: 150px;
    display: flex;
    flex-direction: column;
    justify-content: center;
    font-size: 22px;
    line-height: 1.1;
    color: var(--white);
  }
  .customers { flex: 1; }
  .customers-title { font-size: 16px; margin-bottom: 6px; }
  .customers-list { list-style: none; font-size: 15px; line-height: 1.3; padding-left: 10px; }
  .customers-list li::before { content: "- "; }
  .customers-more { font-size: 15px; margin-top: 4px; padding-left: 20px; }
  .quote-band {
    position: absolute;
    left: 0; right: 0;
    top: 440px;
    height: 54px;
    background: var(--orange);
    color: var(--ink);
    font-size: 19px;
    display: flex;
    align-items: center;
    justify-content: center;
    letter-spacing: .5px;
  }
</style>
</head>
<body>

  <section class="flyer flyer-front">
    <header class="front-header">
      <div class="brand-name">Harbor Quill Dune</div>
      <div class="brand-tagline">electrical and security</div>
    </header>
    <div class="front-body">
      <p class="services-copy">We cover all new electrical installations, repairs, maintenance, renovations/extensions, re-wiring, home theatre, surround sound, wall tv's, electric hot water, stoves, cooktops, lighting, ceiling fans, data, telephone and security systems.</p>
      <div class="call-panel">
        <div class="call-lead">Call us for all</div>
        <div class="call-hours">24/7</div>
        <div class="call-services">emergency<br>services</div>
        <div class="call-divider"></div>
        <div class="call-promise">WE'LL TAKE CARE OF IT FOR YOU!</div>
      </div>
    </div>
    <footer class="front-contact">
      <div class="contact-row">
        <span class="contact-item"><span class="dot-mark"></span>/harborquilldune</span>
        <span class="contact-item">
          <svg width="18" height="18" viewBox="0 0 24 24" aria-hidden="true">
            <circle cx="12" cy="12" r="12" fill="#fff"/>
            <path d="M8.2 5.5l2 2.6-1.2 1.6c.8 1.8 2.3 3.3 4.1 4.1l1.6-1.2 2.6 2-1.1 2.3c-5-.6-9-4.6-9.6-9.6z" fill="#0c0c0c"/>
          </svg>0412555019
        </span>
      </div>
      <div class="contact-web">www.harborquilldune.com.au</div>
    </footer>
  </section>

  <section class="flyer flyer-back">
    <div class="back-photo" role="img" aria-label="Photo of an electrician in a blue work shirt drilling a fitting into a wall"></div>
    <div class="back-body">
      <div class="back-brand">HQD<br>Electrical and Security</div>
      <div class="customers">
        <div class="customers-title">Some of our customers are...</div>
        <ul class="customers-list">
          <li>Bayside College</li>
          <li>Marlow Lounge</li>
          <li>Tidewater Bistro</li>
          <li>Kerbside Tyres</li>
        </ul>
        <div class="customers-more">and many more!</div>
      </div>
    </div>
    <div class="quote-band">Ask us for a quote today!</div>
  </section>

</body>
</html>
```